Plover Scrap Ireland

Hi There,

We are a biofuels company based in Ireland. We produce biodiesel from waste cooking oils from restaurants and biogas from food waste.

We are mainly a B2B company - essentially we take from collectors of these products and they aggregate for us.

We would like to start collections of our own for both waste cooking oil
and food waste from restaurants, hotels, hospitals and offices. We will pay for the waste oil (a main focus) and charge competitive rates for the food waste - all will go to renewable solutions.

Can you design a logo for this business? And then also can you provide a leaflet outline so we can send to businesses/ post on social media. Emphasis should be on the circular model of our business.
Updates

Target Market(s)

Restaurants and Businesses

Industry/Entity Type

Waste Collection

Colors
0094D4
00A9DD
6FCCEA
C7EBF8
E9F6FB
00AB8E
00BBA5
67D7C9
C6EFE9
E9F9F6
59FF00
82FF00
B8FF75
E3FFCB
F4FFEA
FFF300
FFF600
FEFA6F
FFFEC7
FFFEE8

Requirements
Nice to have
• Renewable Ideas, Circular Nature

```html
<!DOCTYPE html>
<html lang="en">
<head>
<meta charset="utf-8">
<title>Plover Scrap Ireland – Leaflet</title>
<link rel="stylesheet" href="https://fonts.googleapis.com/css2?family=Poppins:wght@400;500;600;700;800;900&display=swap">
<style>
  :root {
    --green-deep: #22620a;
    --green-mid: #4f9a0c;
    --lime: #8fd400;
    --lime-light: #a6e21c;
    --forest: #1c4a04;
    --blue: #0b73c7;
    --white: #ffffff;
    --ink: #2c2c2c;
  }
  * { box-sizing: border-box; margin: 0; padding: 0; }
  html, body { width: 915px; height: 1200px; overflow: hidden; background: #ffffff; }
  body { font-family: "Poppins", sans-serif; }
  .leaflet { position: relative; width: 915px; height: 1200px; overflow: hidden; background: var(--white); }
  .backdrop { position: absolute; inset: 0; width: 915px; height: 1200px; }
  .abs { position: absolute; }

  .leaf-placeholder { position: absolute; border-radius: 50% 0 50% 0; }
  .leaf-left { left: -10px; top: 30px; width: 80px; height: 210px; background: radial-gradient(ellipse at 40% 40%, #9fe05a, #4f9a0c 75%); opacity: .75; transform: rotate(-15deg); }
  .leaf-right { left: 808px; top: 214px; width: 120px; height: 150px; background: radial-gradient(ellipse at 50% 40%, #a6e064, #3f8a10 80%); }
  .globe-art { left: 240px; top: 372px; width: 370px; height: 250px; border-radius: 45% 45% 40% 40%; background: radial-gradient(circle at 55% 60%, #a6e21c 0%, #8fd400 45%, rgba(143,212,0,0) 72%); }
  .nozzle-art { left: 0; top: 620px; width: 264px; height: 155px; border-radius: 40px 80px 40px 20px; background: linear-gradient(135deg, #c0410c 0%, #8a2a08 35%, #1e1e1e 65%, #3a3a3a 100%); opacity: .9; }

  .brand-title { left: 0; width: 915px; text-align: center; font-weight: 800; line-height: 1; color: var(--white); text-shadow: 0 6px 14px rgba(0,0,0,.25); }
  .brand-title.line-1 { top: 60px; font-size: 88px; padding-left: 10px; }
  .brand-title.line-2 { top: 128px; font-size: 160px; letter-spacing: -4px; padding-left: 10px; }
  .brand-title.line-3 { top: 278px; font-size: 86px; color: var(--forest); text-shadow: none; letter-spacing: -1px; }

  .produce { left: 58px; top: 276px; width: 190px; color: var(--white); }
  .produce-heading { font-size: 31px; font-weight: 800; line-height: .98; color: var(--lime-light); }
  .produce-intro { margin-top: 14px; font-size: 16px; line-height: 1.22; }
  .produce-rule { height: 1px; background: rgba(255,255,255,.75); margin: 8px 0 8px; width: 143px; }
  .produce-item { display: flex; gap: 10px; align-items: flex-start; font-size: 15px; line-height: 1.2; }
  .produce-item svg { flex: 0 0 26px; margin-top: 2px; }

  .b2b { left: 654px; top: 350px; width: 200px; color: var(--white); }
  .b2b-big { font-size: 56px; font-weight: 800; line-height: 1; color: var(--lime-light); letter-spacing: -1px; }
  .b2b-company { font-size: 35px; font-weight: 800; line-height: 1; margin-top: 2px; }
  .b2b-essentially { font-size: 17px; font-weight: 700; letter-spacing: 4px; color: var(--lime); margin-top: 6px; }
  .b2b-list { list-style: none; margin-top: 14px; font-size: 15px; line-height: 1.2; }
  .b2b-list.second { margin-top: 0; }
  .b2b-list li { display: flex; gap: 8px; }
  .b2b-list li svg { flex: 0 0 12px; margin-top: 4px; }
  .b2b-rule { height: 1px; background: rgba(255,255,255,.8); margin: 12px 0 14px; width: 168px; }

  .collections { left: 366px; top: 722px; color: var(--white); }
  .collections-lead { font-size: 26px; font-weight: 700; color: var(--lime-light); line-height: 1.2; }
  .collections-sub { font-size: 17px; font-weight: 500; line-height: 1.3; }

  .sector { display: flex; align-items: center; gap: 10px; color: var(--white); font-size: 20px; font-weight: 700; }
  .sector-icon { width: 52px; height: 52px; border-radius: 50%; background: var(--lime); display: flex; align-items: center; justify-content: center; }
  .sector.restaurants { left: 499px; top: 814px; }
  .sector.hotels { left: 728px; top: 814px; }
  .sector.hospitals { left: 499px; top: 895px; }
  .sector.offices { left: 728px; top: 898px; }
  .sector-divider { border-top: 1.5px dashed rgba(255,255,255,.8); height: 0; top: 879px; }
  .sector-divider.left { left: 503px; width: 188px; }
  .sector-divider.right { left: 720px; width: 158px; }
  .sector-divider-v { left: 706px; top: 816px; height: 134px; border-left: 1.5px dashed rgba(255,255,255,.8); }

  .pay { left: 46px; top: 794px; font-weight: 800; line-height: .93; font-size: 64px; letter-spacing: -1px; }
  .pay-line-1 { color: var(--forest); }
  .pay-line-2 { color: #2b2b2b; }
  .pay-badge { left: 46px; top: 915px; width: 254px; height: 36px; background: var(--lime); border: 2px solid #6aa800; border-radius: 3px; color: var(--forest); font-size: 22px; font-weight: 800; letter-spacing: 4px; display: flex; align-items: center; justify-content: center; }
  .pay-note { left: 47px; top: 966px; width: 360px; font-size: 15px; font-weight: 600; line-height: 1.4; color: var(--ink); }

  .signature { left: 40px; top: 1086px; display: flex; align-items: center; gap: 14px; }
  .signature-mark { width: 62px; height: 62px; border-radius: 50%; background: var(--blue); }
  .signature-name { font-size: 24px; font-weight: 600; color: #1e1e1e; letter-spacing: 1px; line-height: 1; }

  .contact-phone { left: 449px; top: 1082px; display: flex; align-items: center; gap: 12px; font-size: 44px; font-weight: 800; color: #2a2a2a; line-height: 1; letter-spacing: 1px; }
  .contact-phone-icon { width: 40px; height: 40px; border-radius: 50%; background: var(--forest); display: flex; align-items: center; justify-content: center; }
  .contact-web { left: 455px; top: 1136px; font-size: 24px; font-weight: 700; color: var(--forest); letter-spacing: 1.5px; line-height: 1; }
  .contact-web .prefix { color: #2a2a2a; }
</style>
</head>
<body>
<main class="leaflet">
  <svg class="backdrop" viewBox="0 0 915 1200" preserveAspectRatio="none" aria-hidden="true">
    <defs>
      <radialGradient id="greenField" cx="0.55" cy="0.55" r="0.75">
        <stop offset="0" stop-color="#7fc414"/>
        <stop offset="0.55" stop-color="#3f8a0a"/>
        <stop offset="1" stop-color="#1f5e06"/>
      </radialGradient>
      <linearGradient id="blueField" x1="0" y1="0" x2="1" y2="0.6">
        <stop offset="0" stop-color="#0a4a96"/>
        <stop offset="0.6" stop-color="#0b6fc4"/>
        <stop offset="1" stop-color="#0a9ae4"/>
      </linearGradient>
    </defs>
    <rect x="0" y="0" width="915" height="730" fill="url(#greenField)"/>
    <path d="M0 770 C80 720 200 645 260 630 C290 660 310 705 325 750 C345 800 370 830 410 850 C445 870 460 905 490 940 C520 975 560 1005 620 1015 L620 1200 H0 Z" fill="#ffffff"/>
    <path d="M352 832 C395 842 435 862 458 902 C425 880 390 862 352 832 Z" fill="var(--lime)"/>
    <path d="M480 950 C540 1010 620 1040 720 1045 C800 1048 870 1035 915 1028 V1042 C860 1054 780 1064 700 1060 C600 1054 530 1012 480 950 Z" fill="var(--lime)"/>
    <path d="M260 630 C300 625 320 650 350 645 C400 640 430 610 465 612 C510 615 540 680 590 690 C650 700 700 660 740 662 C780 664 790 720 820 712 C860 700 890 670 915 660 V1010 C820 1020 700 1030 620 1015 C560 1005 520 975 490 940 C460 905 445 870 410 850 C370 830 345 800 325 750 C310 705 290 660 260 630 Z" fill="url(#blueField)" stroke="#ffffff" stroke-width="5"/>
  </svg>

  <div class="leaf-placeholder leaf-left" role="img" aria-label="Soft-focus green leaf"></div>
  <div class="leaf-placeholder leaf-right" role="img" aria-label="Fresh green leaf"></div>
  <div class="abs globe-art" role="img" aria-label="Lime green globe with leaves sprouting on top"></div>
  <div class="abs nozzle-art" role="img" aria-label="Fuel pump nozzle with a green seedling growing from its spout"></div>

  <h1>
    <span class="abs brand-title line-1">PLOVER</span>
    <span class="abs brand-title line-2">SCRAP</span>
    <span class="abs brand-title line-3">IRELAND</span>
  </h1>

  <section class="abs produce">
    <h2 class="produce-heading">We<br>produce</h2>
    <p class="produce-intro">biodiesel from<br>waste cooking<br>oils from</p>
    <div class="produce-rule"></div>
    <div class="produce-item">
      <svg width="26" height="36" viewBox="0 0 26 36" aria-hidden="true"><path d="M9 2h6v6c6 3 9 9 9 15 0 7-5 11-11 11S2 30 2 23c0-6 3-12 7-15z" fill="var(--lime)"/></svg>
      <span>Waste cooking<br>oils from<br>restaurants</span>
    </div>
    <div class="produce-rule"></div>
    <div class="produce-item">
      <svg width="26" height="30" viewBox="0 0 26 30" aria-hidden="true"><path d="M3 9h20l-2 19H5z M1 6h24v3H1z" fill="none" stroke="var(--lime)" stroke-width="2.5"/><path d="M10 13v11M16 13v11" stroke="var(--lime)" stroke-width="2"/></svg>
      <span>Biogas from<br>food waste</span>
    </div>
  </section>

  <section class="abs b2b">
    <div class="b2b-big">B2B</div>
    <div class="b2b-company">COMPANY</div>
    <div class="b2b-essentially">ESSENTIALLY</div>
    <ul class="b2b-list">
      <li><svg width="12" height="12" viewBox="0 0 12 12" aria-hidden="true"><circle cx="6" cy="6" r="6" fill="var(--lime)"/><path d="M3 6l2 2 4-4" stroke="#2a6a00" stroke-width="1.6" fill="none"/></svg><span>we take from<br>collectors<br>of these products</span></li>
    </ul>
    <div class="b2b-rule"></div>
    <ul class="b2b-list second">
      <li><svg width="12" height="12" viewBox="0 0 12 12" aria-hidden="true"><circle cx="6" cy="6" r="6" fill="var(--lime)"/><path d="M3 6l2 2 4-4" stroke="#2a6a00" stroke-width="1.6" fill="none"/></svg><span>And they aggregate<br>for us.</span></li>
    </ul>
  </section>

  <section class="abs collections">
    <p class="collections-lead">We would like to start</p>
    <p class="collections-sub">collections of our own for both waste cooking oil from</p>
  </section>

  <div class="abs sector restaurants"><span class="sector-icon"><svg width="28" height="26" viewBox="0 0 28 26" aria-hidden="true"><path d="M2 2h24v6H2z M4 8h20v16H4z" fill="none" stroke="#1c4a04" stroke-width="2"/><path d="M7 14h6v10H7z M16 13h5v5h-5z" fill="#1c4a04"/></svg></span>Restaurants</div>
  <div class="abs sector hotels"><span class="sector-icon"><svg width="26" height="28" viewBox="0 0 26 28" aria-hidden="true"><path d="M5 6h16v20H5z" fill="none" stroke="#1c4a04" stroke-width="2"/><path d="M9 10h3v3H9zM14 10h3v3h-3zM9 16h3v3H9zM14 16h3v3h-3zM11 22h4v4h-4z" fill="#1c4a04"/></svg></span>Hotels</div>
  <div class="abs sector hospitals"><span class="sector-icon"><svg width="26" height="28" viewBox="0 0 26 28" aria-hidden="true"><path d="M8 4h14v22H8z" fill="none" stroke="#1c4a04" stroke-width="2"/><path d="M13 8h4v2h2v3h-2v2h-4v-2h-2v-3h2z" fill="#1c4a04"/><circle cx="5" cy="20" r="3" fill="none" stroke="#1c4a04" stroke-width="2"/></svg></span>Hospitals</div>
  <div class="abs sector offices"><span class="sector-icon"><svg width="26" height="28" viewBox="0 0 26 28" aria-hidden="true"><path d="M4 8h18v18H4z M7 3h12v5H7z" fill="none" stroke="#1c4a04" stroke-width="2"/><path d="M8 12h3v3H8zM15 12h3v3h-3zM8 18h3v3H8zM15 18h3v3h-3z" fill="#1c4a04"/></svg></span>Offices</div>
  <div class="abs sector-divider left"></div>
  <div class="abs sector-divider right"></div>
  <div class="abs sector-divider-v"></div>

  <section>
    <h2 class="abs pay"><span class="pay-line-1">WE WILL</span><br><span class="pay-line-2">PAY FOR</span></h2>
    <div class="abs pay-badge">THE WASTE OIL</div>
    <p class="abs pay-note">And charge competitive rates for the food waste - all will go to renewable solutions.</p>
  </section>

  <div class="abs signature">
    <span class="signature-mark" aria-hidden="true"></span>
    <span class="signature-name">PLOVER SCRAP IRELAND</span>
  </div>

  <div class="abs contact-phone">
    <span class="contact-phone-icon"><svg width="22" height="22" viewBox="0 0 24 24" aria-hidden="true"><path d="M6.6 10.8a15 15 0 006.6 6.6l2.2-2.2c.3-.3.7-.4 1-.2 1.1.4 2.3.6 3.6.6.6 0 1 .4 1 1V20c0 .6-.4 1-1 1A17 17 0 013 4c0-.6.4-1 1-1h3.5c.6 0 1 .4 1 1 0 1.3.2 2.5.6 3.6.1.3 0 .7-.2 1z" fill="#ffffff"/></svg></span>
    555 0142 7730
  </div>
  <div class="abs contact-web"><span class="prefix">www.</span>ploverscrapireland<span class="prefix">.com</span></div>
</main>
</body>
</html>
```